Registration Page - Webinar

I need some proposition for a high conversion landing page for a Webinar.
This LP should follow some (minimal) rules:
1 - We need to have a registration box at it
2 - 1, 2 or 3 Keynote Speakers
3 - Featuring Time & Date
4 - All webinars will be free
5 - Title of the webinar
6 - Description of the webinar
7 - Should harmonize with my home page colors (www.themarbleharbor.com)

```html
<!DOCTYPE html>
<html lang="pt">
<head>
<meta charset="utf-8">
<title>Marble Harbor — Webinar Registration</title>
<link href="https://fonts.googleapis.com/css2?family=Poppins:wght@400;500;600;700;800&family=Open+Sans:wght@400&display=swap" rel="stylesheet">
<style>
:root{
  --pink:#e5086f;
  --magenta:#d21d55;
  --orange:#f47b20;
  --cyan:#22b5d3;
  --green:#1bb33a;
  --navy:#3a2b6e;
  --ink:#111;
  --body:#555;
  --footer-bg:#efeff0;
  --bar:#1e1e1e;
  --white:#fff;
}
*{margin:0;padding:0;box-sizing:border-box}
html,body{width:718px;height:1200px;overflow:hidden;background:var(--white)}
body{position:relative;font-family:"Poppins",sans-serif;color:var(--ink)}
.abs{position:absolute}

/* top nav */
.topnav{left:0;top:0;width:718px;height:30px;background:var(--pink)}
.topnav a{position:absolute;top:8px;font-size:7.6px;font-weight:600;color:var(--white);text-decoration:none;letter-spacing:.1px}
.social{top:11px;width:9px;height:9px;border-radius:50%;background:var(--white)}

/* header */
.header{left:0;top:30px;width:718px;height:53px;background:var(--white);border-bottom:1px solid #ddd}
.bump{left:302px;top:70px;width:102px;height:33px;background:var(--white);border-radius:0 0 51px 51px/0 0 33px 33px;box-shadow:0 2px 2px rgba(0,0,0,.08);z-index:3}
.hotline{height:15px;background:var(--green);border-radius:2px;color:var(--white);font-weight:700;display:flex;align-items:center;gap:4px;padding:0 5px;white-space:nowrap}
.hotline svg{width:9px;height:9px;flex:none}
.phones{font-size:7.6px;color:var(--navy);display:flex;align-items:center;gap:4px;white-space:nowrap}
.dot{width:8px;height:8px;border-radius:50%;display:inline-block}
.dot.br{background:var(--green)}
.dot.us{background:#c93a4a}
.brand{font-weight:800;color:var(--pink);text-align:center;letter-spacing:.5px;line-height:1}
.action{display:flex;align-items:center;gap:5px}
.action .ic{width:23px;height:23px;border-radius:50%;display:flex;align-items:center;justify-content:center;flex:none}
.action .ic svg{width:12px;height:12px}
.action span{font-size:7.8px;font-weight:700;line-height:1;color:var(--navy);white-space:nowrap}

/* hero */
.hero{left:0;top:83px;width:718px;height:327px;background:
  radial-gradient(ellipse 130px 110px at 270px 60px,rgba(214,170,140,.55),transparent 70%),
  radial-gradient(ellipse 160px 150px at 420px 140px,rgba(120,70,40,.6),transparent 70%),
  linear-gradient(100deg,#3d4452 0%,#6a5a4e 35%,#5a4538 55%,#3a3530 80%,#2c2b2e 100%)}
.hero-title{left:69px;top:173px;font-size:19.5px;font-weight:700;line-height:23.5px;color:var(--white)}
.pill{left:69px;width:180px;height:31px;border-radius:16px;background:var(--magenta);display:flex;align-items:center;gap:7px;padding-left:4px;color:var(--white);font-weight:600;font-size:12.5px;white-space:nowrap}
.pill .ic{width:24px;height:24px;border-radius:50%;background:var(--cyan);display:flex;align-items:center;justify-content:center;flex:none}
.pill .ic svg{width:12px;height:12px}
.count{top:311px;width:43px;height:42px;border:1px solid var(--white);border-radius:2px;color:var(--white);text-align:center}
.count b{display:block;font-size:20px;font-weight:700;line-height:22px;margin-top:4px}
.count small{display:block;font-size:8.5px;font-weight:700;line-height:10px}
.free-tab{left:58px;top:377px;width:190px;height:33px;background:var(--orange);border-radius:28px 28px 0 0/33px 33px 0 0;color:var(--white);font-size:11px;font-weight:700;text-align:center;line-height:33px}

/* registration */
.register{left:422px;top:119px;width:219px;height:252px;background:rgba(34,181,211,.9)}
.register h2{position:absolute;left:33px;top:18px;font-size:14.5px;font-weight:700;color:var(--white);white-space:nowrap}
.field{position:absolute;left:20px;width:179px;height:24px;border:1px solid var(--white);font-size:7.6px;color:var(--white);padding-left:12px;line-height:22px}
.btn{position:absolute;left:20px;top:199px;width:179px;height:31px;background:var(--orange);color:var(--white);font-size:10px;font-weight:700;text-align:center;line-height:31px}

/* description */
.desc-title{left:72px;top:466px;font-size:15px;font-weight:700;color:var(--ink)}
.rule{height:2px;background:var(--magenta)}
.desc-body{left:72px;top:503px;width:272px;font-family:"Open Sans",sans-serif;font-size:8.4px;line-height:12.6px;color:var(--body)}
.desc-body p{margin-bottom:6.3px}
.desc-photo{left:368px;top:471px;width:280px;height:222px;background:
  radial-gradient(ellipse 120px 90px at 60px 90px,rgba(255,220,150,.95),transparent 70%),
  linear-gradient(180deg,#d8a862 0%,#b07a3c 55%,#6d5026 100%);box-shadow:0 0 14px rgba(0,0,0,.15)}

/* speakers */
.speakers{left:0;top:747px;width:718px;height:260px;background:linear-gradient(90deg,#f47b22 0%,#e9533a 45%,#d21f4f 100%)}
.speakers h2{position:absolute;left:0;width:718px;top:26px;text-align:center;font-size:15.5px;font-weight:700;color:var(--white)}
.speaker-photo{top:835px;width:84px;height:84px;border-radius:50%;background:linear-gradient(160deg,#d9dde2,#8c96a3)}
.speaker{top:838px;width:98px;color:var(--white)}
.speaker h3{font-size:13.5px;font-weight:700;line-height:17px;white-space:nowrap}
.speaker h4{font-size:7.4px;font-weight:700;line-height:10px;margin-top:1px}
.speaker p{font-family:"Open Sans",sans-serif;font-size:7.2px;line-height:10.2px;margin-top:6px}
.skyline{left:0;top:956px;width:718px;height:46px}

/* footer */
.footer{left:0;top:1000px;width:718px;height:170px;background:var(--footer-bg)}
.loc{left:74px;color:var(--navy)}
.loc h5{font-size:8.6px;font-weight:600;display:flex;align-items:center;gap:5px}
.loc h5 svg{width:6px;height:8px}
.loc p{font-size:6.4px;line-height:11px}
.mail{left:74px;top:1132px;font-size:9px;font-weight:600;color:var(--navy);display:flex;align-items:center;gap:4px}
.bar{left:0;top:1170px;width:718px;height:30px;background:var(--bar)}
.bar .copy{position:absolute;left:74px;top:11px;font-size:5.4px;font-weight:700;color:var(--white)}
.bar .copy span{color:var(--pink);font-weight:500}
.bar a{position:absolute;top:11px;font-size:5.4px;font-weight:700;color:var(--white);text-decoration:none}
</style>
</head>
<body>

<nav class="abs topnav">
  <a style="left:49px">HOME</a>
  <a style="left:90px">SOBRE NÓS</a>
  <a style="left:150px">PORTIFÓLIO</a>
  <a style="left:210px">IMÓVEIS</a>
  <a style="left:259px">NOTÍCIAS</a>
  <a style="left:313px">EBOOKS</a>
  <a style="left:361px">CONTATO</a>
  <span class="abs social" style="left:616px"></span>
  <span class="abs social" style="left:634px"></span>
  <span class="abs social" style="left:652px"></span>
</nav>

<header class="abs header"></header>
<div class="abs bump"></div>

<div class="abs hotline" style="left:86px;top:42px;font-size:7.2px">
  <svg viewBox="0 0 24 24" fill="#fff"><path d="M6.6 10.8a15.1 15.1 0 0 0 6.6 6.6l2.2-2.2a1 1 0 0 1 1-.25 11.4 11.4 0 0 0 3.6.6 1 1 0 0 1 1 1V20a1 1 0 0 1-1 1A17 17 0 0 1 3 4a1 1 0 0 1 1-1h3.5a1 1 0 0 1 1 1c0 1.25.2 2.45.6 3.6a1 1 0 0 1-.25 1z"/></svg>
  EUA +1 (407) 555-0142
</div>
<div class="abs phones" style="left:56px;top:63px">
  <i class="dot br"></i>+55 21 5550-1932 &nbsp;&nbsp;<i class="dot us"></i>+1 (855) 555-0177
</div>

<div class="abs brand" style="left:290px;top:46px;width:134px;font-size:18px;z-index:4">MARBLE<br>HARBOR</div>

<div class="abs action" style="left:470px;top:46px">
  <div class="ic" style="background:var(--pink)"><svg viewBox="0 0 24 24" fill="none" stroke="#fff" stroke-width="2"><path d="M4 5h16v10H9l-4 4v-4H4z"/></svg></div>
  <span>FALE COM UM<br>AGENTE</span>
</div>
<div class="abs action" style="left:569px;top:46px">
  <div class="ic" style="background:var(--cyan)"><svg viewBox="0 0 24 24" fill="none" stroke="#fff" stroke-width="2"><rect x="3" y="5" width="18" height="16" rx="2"/><path d="M3 10h18M8 3v4M16 3v4"/></svg></div>
  <span>AGENDE UMA<br>CONVERSA</span>
</div>

<section class="abs hero" role="img" aria-label="Photo of two colleagues smiling and working together at a table"></section>

<h1 class="abs hero-title">AUGIAT IN PEDE FUSCE TELLUS<br>SED METUS AUGUE</h1>

<div class="abs pill" style="top:229px">
  <div class="ic"><svg viewBox="0 0 24 24" fill="none" stroke="#fff" stroke-width="2"><rect x="3" y="5" width="18" height="16" rx="2"/><path d="M3 10h18M8 3v4M16 3v4"/></svg></div>
  Friday, 17 March 2020
</div>
<div class="abs pill" style="top:266px">
  <div class="ic"><svg viewBox="0 0 24 24" fill="none" stroke="#fff" stroke-width="2"><circle cx="12" cy="12" r="9"/><path d="M12 7v5l3 2"/></svg></div>
  10: 00 am to 01:00 pm
</div>

<div class="abs count" style="left:70px"><b>10</b><small>DAYS</small></div>
<div class="abs count" style="left:117px"><b>08</b><small>HOUR</small></div>
<div class="abs count" style="left:163px"><b>10</b><small>MIN</small></div>
<div class="abs count" style="left:210px"><b>55</b><small>SEC</small></div>

<div class="abs free-tab">All Webinar are Free</div>

<form class="abs register">
  <h2>REGISTERATION NOW</h2>
  <div class="field" style="top:47px">First Name</div>
  <div class="field" style="top:76.5px">Last Name</div>
  <div class="field" style="top:106px">Email address</div>
  <div class="field" style="top:136px">Phone</div>
  <div class="field" style="top:165.5px">Company</div>
  <div class="btn">REGISTER</div>
</form>

<h2 class="abs desc-title">WEBINAR DESCRIPTION</h2>
<div class="abs rule" style="left:75px;top:489px;width:30px"></div>
<div class="abs desc-body">
  <p>Augiat in pede Fusce tellus Sed metus augue convallis et vehicula ut pulvinar eu ante Integer orci tellus tristique vitae consequat nec mauris viverra in gravida eu mattis in ante Morbi eget</p>
  <p>Fusce ultricies orci ac feugiat suscipit leo massa sodales velit et scelerisque mi tortor at ipsum Proin orci odio commodo ac gravida non tristique vel te Curabitur iaculis tempus eros Curabitur vel mi sit amet magna malesuada ultrices Ut nisi erat fermentum vel congue id euismod in elit Fusce ultricies orci ac feugiat suscipit</p>
  <p>scelerisque quam Curabitur vel dolor ultrices ipsum dictum tristique Praesent vitae lacus Ut velit enim vestibulum non fermentum nec hendrerit quis leo Pellentesque rutrum malesuada neque Nunc tempus felis vitae urna Vivamus porttitor neque at volutpat rutrum purus nisi eleifend libero a tempus libero lectus feugiat felis Morbi diam mauris viverra in gravida eu mattis in anquam Curabitur vel</p>
</div>
<div class="abs desc-photo" role="img" aria-label="Photo of a family running with a kite in a field at sunset"></div>

<section class="abs speakers"><h2>KEYNOTE SPEAKERS</h2></section>
<div class="abs rule" style="left:335px;top:798px;width:28px;background:var(--white)"></div>

<div class="abs speaker-photo" style="left:69px" role="img" aria-label="Portrait photo of speaker Dave Elvis"></div>
<div class="abs speaker" style="left:160px"><h3>Dave Elvis</h3><h4>Subject Title</h4><p>Curabitur vel dolor ultrices ipsum dictum tristique Praesent vitae lacus Ut velit enim vestibulum</p></div>

<div class="abs speaker-photo" style="left:275px" role="img" aria-label="Portrait photo of speaker Rober Will"></div>
<div class="abs speaker" style="left:366px"><h3>Rober Will</h3><h4>Subject Title</h4><p>Curabitur vel dolor ultrices ipsum dictum tristique Praesent vitae lacus Ut velit enim vestibulum</p></div>

<div class="abs speaker-photo" style="left:480px" role="img" aria-label="Portrait photo of speaker Susan"></div>
<div class="abs speaker" style="left:571px"><h3>Susan</h3><h4>Subject Title</h4><p>Curabitur vel dolor ultrices ipsum dictum tristique Praesent vitae lacus Ut velit enim vestibulum</p></div>

<div class="abs skyline" role="img" aria-label="City skyline silhouette illustration" style="background:linear-gradient(180deg,rgba(239,239,240,0) 0%,rgba(239,239,240,.7) 45%,var(--footer-bg) 100%)"></div>

<footer class="abs footer"></footer>

<div class="abs loc" style="top:1016px">
  <h5><svg viewBox="0 0 12 16" fill="#e5086f"><path d="M6 0a6 6 0 0 0-6 6c0 4.5 6 10 6 10s6-5.5 6-10a6 6 0 0 0-6-6zm0 8.5A2.5 2.5 0 1 1 6 3.5a2.5 2.5 0 0 1 0 5z"/></svg>Harbor Point Barra</h5>
  <p>2º Piso ao lado do Café Lume Av. das Ondas 4120,<br>Barra da Tijuca - RJ - Brasil</p>
</div>
<div class="abs loc" style="top:1060px">
  <h5><svg viewBox="0 0 12 16" fill="#e5086f"><path d="M6 0a6 6 0 0 0-6 6c0 4.5 6 10 6 10s6-5.5 6-10a6 6 0 0 0-6-6zm0 8.5A2.5 2.5 0 1 1 6 3.5a2.5 2.5 0 0 1 0 5z"/></svg>Shopping Vila Serena</h5>
  <p>Av. Das Palmeiras, 3150 210/211 Alto de<br>Pinheiros - São Paulo - Brasil</p>
</div>
<div class="abs loc" style="top:1103px">
  <h5><svg viewBox="0 0 12 16" fill="#e5086f"><path d="M6 0a6 6 0 0 0-6 6c0 4.5 6 10 6 10s6-5.5 6-10a6 6 0 0 0-6-6zm0 8.5A2.5 2.5 0 1 1 6 3.5a2.5 2.5 0 0 1 0 5z"/></svg>Orlando</h5>
  <p>4820 Coral Bay Avenue, Suite 212, Orlando, EUA</p>
</div>
<div class="abs mail">
  <svg width="10" height="8" viewBox="0 0 20 16" fill="#e5086f"><path d="M0 0h20v16H0z"/><path d="M0 0l10 8 10-8" fill="none" stroke="#efeff0" stroke-width="2"/></svg>
  contact@themarbleharbor.com
</div>

<div class="abs brand" style="left:278px;top:1034px;width:134px;font-size:18px">MARBLE<br>HARBOR</div>

<div class="abs hotline" style="left:462px;top:1014px;height:18px;font-size:9.2px">
  <svg viewBox="0 0 24 24" fill="#fff"><path d="M6.6 10.8a15.1 15.1 0 0 0 6.6 6.6l2.2-2.2a1 1 0 0 1 1-.25 11.4 11.4 0 0 0 3.6.6 1 1 0 0 1 1 1V20a1 1 0 0 1-1 1A17 17 0 0 1 3 4a1 1 0 0 1 1-1h3.5a1 1 0 0 1 1 1c0 1.25.2 2.45.6 3.6a1 1 0 0 1-.25 1z"/></svg>
  EUA +1 (407) 555-0142
</div>
<div class="abs phones" style="left:453px;top:1038px">
  <i class="dot br"></i>+55 21 5550-1932 &nbsp;<i class="dot us"></i>+1 (855) 555-0177
</div>
<div class="abs action" style="left:445px;top:1063px">
  <div class="ic" style="background:var(--pink)"><svg viewBox="0 0 24 24" fill="none" stroke="#fff" stroke-width="2"><path d="M4 5h16v10H9l-4 4v-4H4z"/></svg></div>
  <span style="font-size:8px">FALE COM UM<br>AGENTE</span>
</div>
<div class="abs action" style="left:531px;top:1063px">
  <div class="ic" style="background:var(--cyan)"><svg viewBox="0 0 24 24" fill="none" stroke="#fff" stroke-width="2"><rect x="3" y="5" width="18" height="16" rx="2"/><path d="M3 10h18M8 3v4M16 3v4"/></svg></div>
  <span style="font-size:8px">AGENDE UMA<br>CONVERSA</span>
</div>

<div class="abs bar">
  <div class="copy">© 2017 - THE MARBLE HARBOR BY <span>NORTHPIXEL</span></div>
  <a style="left:411px;color:var(--pink);font-weight:500">HOME</a>
  <a style="left:446px">IMÓVEIS</a>
  <a style="left:487px">NOTÍCIAS</a>
  <a style="left:532px">CONTATO</a>
  <a style="left:577px">TERMS OF USE</a>
</div>

</body>
</html>
```